Vehicle Wrapping for Velmar Cargoline Van for company "Harlow Plumbing"

Vehicle Rap for Harlow Plumbing.
Feature the Green Colour on website and Logo
Maybe use baby picture from Website.
Services
Drain Cleaning Services
Electric Water Heater Services
Hydro Jetting Services
Kitchen Services
Root Removal
Sump Pump Contractor
Sump Pump Contractor
Water Treatment
Clogged Toilet Repair
Root Removal
Fixture Installation & Repair
Plumbing Maintenance
Plumbing Inspections
Emergency Plumbing

Target Market(s)

Residential and Commericial Plumbing Customers

Industry/Entity Type

Residential and Commercial Plumbing

Font styles to use
Sans Serif

Colors
59FF00
82FF00
B8FF75
E3FFCB
F4FFEA

Requirements
Must have
• Green Colour for Vehicle. Phone number on side of Van. Email on side of Van.
Nice to have
• Maybe using the baby picture from the website.

```html
<!DOCTYPE html>
<html lang="en">
<head>
<meta charset="utf-8">
<title>Harlow Plumbing – Velmar Cargoline Van Wrap</title>
<link rel="stylesheet" href="https://fonts.googleapis.com/css2?family=Open+Sans:wght@400;600;700&family=PT+Sans+Narrow:wght@400;700&display=swap">
<style>
  :root {
    --ink: #0b0f1a;
    --green: #1f8f1c;
    --green-bright: #3fbf2a;
    --white: #ffffff;
    --muted: #b9bcc2;
    --paper: #ededed;
    --stage-dark: #444444;
    --text-dark: #14181f;
  }
  * { margin: 0; padding: 0; box-sizing: border-box; }
  html, body { width: 867px; height: 1200px; overflow: hidden; background: var(--paper); }
  .wrap-sheet { position: relative; width: 867px; height: 1200px; font-family: "Open Sans", sans-serif; }
  .band { position: absolute; left: 0; width: 867px; }
  .band--side-right { top: 0; height: 370px; background: linear-gradient(#e4e4e4, #f3f3f3); }
  .band--rear { top: 370px; height: 460px; background: var(--stage-dark); }
  .band--side-left { top: 830px; height: 370px; background: linear-gradient(#e4e4e4, #f3f3f3); }
  .side-panel { position: absolute; left: 40px; top: 40px; width: 787px; height: 290px; }
  .rear-panel { position: absolute; left: 223px; top: 20px; width: 420px; height: 420px; }
  .web { font-family: "Open Sans", sans-serif; font-size: 20px; font-weight: 600; }
  .web--rear { font-family: "PT Sans Narrow", sans-serif; font-size: 24px; font-weight: 700; }
  .brand-name { font-family: "Open Sans", sans-serif; font-weight: 700; fill: var(--white); }
  .contact { font-family: "Open Sans", sans-serif; font-size: 17px; font-weight: 600; fill: var(--text-dark); }
  .contact--rear { font-family: "PT Sans Narrow", sans-serif; font-size: 14px; fill: var(--white); font-weight: 400; }
  .services-title { font-family: "PT Sans Narrow", sans-serif; font-weight: 700; font-size: 36px; fill: var(--green-bright); }
  .service-item { font-family: "PT Sans Narrow", sans-serif; font-size: 13px; fill: var(--muted); }
  .fill-ink { fill: var(--ink); }
  .fill-green { fill: var(--green); }
  .fill-green-bright { fill: var(--green-bright); }
  .fill-white { fill: var(--white); }
</style>
</head>
<body>
<main class="wrap-sheet">

  <section class="band band--side-right" aria-label="Passenger side wrap">
    <svg class="side-panel" viewBox="0 0 787 290" xmlns="http://www.w3.org/2000/svg">
      <defs>
        <linearGradient id="photo-tones" x1="0" y1="0" x2="0" y2="1">
          <stop offset="0" stop-color="#6fae3c"/>
          <stop offset="0.35" stop-color="#a9bfa0"/>
          <stop offset="0.7" stop-color="#e2cbbb"/>
          <stop offset="1" stop-color="#f4f2ef"/>
        </linearGradient>
      </defs>
      <path class="fill-ink" d="M0 0 H300 C272 95 272 195 300 290 H0Z"/>
      <path class="fill-green" d="M300 0 H322 C294 95 294 195 322 290 H300 C272 195 272 95 300 0Z"/>
      <path role="img" aria-label="Photo of a laughing baby splashing under a kitchen faucet" fill="url(#photo-tones)" d="M322 0 H787 V290 H322 C294 195 294 95 322 0Z"/>

      <text class="web" x="36" y="32"><tspan fill="var(--green-bright)">www.harlow</tspan><tspan fill="var(--white)">plumbing.ca</tspan></text>
      <rect class="fill-green" x="36" y="70" width="70" height="70"/>
      <text class="brand-name" x="36" y="200" font-size="40">HARLOW</text>
      <text class="brand-name" x="36" y="246" font-size="40">PLUMBING</text>

      <g class="contact-line">
        <circle class="fill-green-bright" cx="380" cy="262" r="9"/>
        <path class="fill-white" d="M376 257 l3 -1 l2 4 l-2 1 q1 3 4 4 l1 -2 l4 2 l-1 3 q-8 0 -11 -11z"/>
        <text class="contact" x="396" y="268">613-555-0147</text>
        <circle class="fill-green-bright" cx="536" cy="262" r="9"/>
        <rect class="fill-white" x="530" y="258" width="12" height="8" rx="1"/>
        <text class="contact" x="552" y="268">info@harlowplumbing.ca</text>
      </g>
    </svg>
  </section>

  <section class="band band--rear" aria-label="Rear doors wrap">
    <svg class="rear-panel" viewBox="0 0 420 420" xmlns="http://www.w3.org/2000/svg">
      <rect class="fill-ink" x="0" y="0" width="420" height="420" rx="18"/>
      <text class="web web--rear" x="24" y="44"><tspan fill="var(--green-bright)">WWW.HARLOW</tspan><tspan fill="var(--white)">PLUMBING.CA</tspan></text>

      <rect class="fill-green" x="24" y="78" width="46" height="46"/>
      <text class="brand-name" x="24" y="154" font-size="20">HARLOW</text>
      <text class="brand-name" x="24" y="178" font-size="20">PLUMBING</text>

      <text class="services-title" x="396" y="110" text-anchor="end">Services</text>
      <g class="services-list" text-anchor="end">
        <text class="service-item" x="396" y="146">Drain Cleaning Services</text>
        <text class="service-item" x="396" y="164">Electric Water Heater Services</text>
        <text class="service-item" x="396" y="182">Hydro Jetting Services</text>
        <text class="service-item" x="396" y="200">Kitchen Services</text>
        <text class="service-item" x="396" y="218">Root Removal</text>
        <text class="service-item" x="396" y="236">Sump Pump Contractor</text>
        <text class="service-item" x="396" y="254">Sump Pump Contractor</text>
        <text class="service-item" x="396" y="272">Water Treatment</text>
        <text class="service-item" x="396" y="290">Clogged Toilet Repair</text>
        <text class="service-item" x="396" y="308">Root Removal</text>
        <text class="service-item" x="396" y="326">Fixture Installation &amp; Repair</text>
        <text class="service-item" x="396" y="344">Plumbing Maintenance</text>
        <text class="service-item" x="396" y="362">Plumbing Inspections</text>
        <text class="service-item" x="396" y="380">Emergency Plumbing</text>
      </g>

      <g class="contact-block">
        <circle class="fill-green-bright" cx="31" cy="362" r="6"/>
        <text class="contact contact--rear" x="44" y="367">613-555-0147</text>
        <circle class="fill-green-bright" cx="31" cy="384" r="6"/>
        <text class="contact contact--rear" x="44" y="389">info@harlowplumbing.ca</text>
      </g>
    </svg>
  </section>

  <section class="band band--side-left" aria-label="Driver side wrap">
    <svg class="side-panel" viewBox="0 0 787 290" xmlns="http://www.w3.org/2000/svg">
      <defs>
        <linearGradient id="photo-tones-left" x1="0" y1="0" x2="0" y2="1">
          <stop offset="0" stop-color="#6fae3c"/>
          <stop offset="0.35" stop-color="#a9bfa0"/>
          <stop offset="0.7" stop-color="#e2cbbb"/>
          <stop offset="1" stop-color="#f4f2ef"/>
        </linearGradient>
      </defs>
      <g transform="translate(787 0) scale(-1 1)">
        <path class="fill-ink" d="M0 0 H300 C272 95 272 195 300 290 H0Z"/>
        <path class="fill-green" d="M300 0 H322 C294 95 294 195 322 290 H300 C272 195 272 95 300 0Z"/>
        <path role="img" aria-label="Photo of a laughing baby splashing under a kitchen faucet" fill="url(#photo-tones-left)" d="M322 0 H787 V290 H322 C294 195 294 95 322 0Z"/>
      </g>

      <text class="web" x="751" y="32" text-anchor="end"><tspan fill="var(--green-bright)">www.harlow</tspan><tspan fill="var(--white)">plumbing.ca</tspan></text>
      <rect class="fill-green" x="524" y="70" width="70" height="70"/>
      <text class="brand-name" x="524" y="200" font-size="40">HARLOW</text>
      <text class="brand-name" x="524" y="246" font-size="40">PLUMBING</text>

      <g class="contact-line">
        <circle class="fill-green-bright" cx="60" cy="262" r="9"/>
        <path class="fill-white" d="M56 257 l3 -1 l2 4 l-2 1 q1 3 4 4 l1 -2 l4 2 l-1 3 q-8 0 -11 -11z"/>
        <text class="contact" x="76" y="268">613-555-0147</text>
        <circle class="fill-green-bright" cx="212" cy="262" r="9"/>
        <rect class="fill-white" x="206" y="258" width="12" height="8" rx="1"/>
        <text class="contact" x="228" y="268">info@harlowplumbing.ca</text>
      </g>
    </svg>
  </section>

</main>
</body>
</html>
```